Cleaning Bochure for Different Services

We need to create preferably an A4 brochure for cleaning services so we are able to give to our customers upon meeting them. check out our website for more info. It is www.brightvaleservices.co.uk We need a page on;-Commercial Cleaning-Carpet Cleaning-Oven Cleaning with description and some imagery.

Target Market(s)

Commercial Cleaning Customers

Industry/Entity Type

Office Cleaning

Font styles to use
Sans Serif

Colors
33a6d7
aaaaaa

Requirements
Must have
• 4 pages each containing these services
• -Commercial Cleaning (most important)
• -Carpet Cleaning
• -Oven Cleaning
Nice to have
• Clean and smart looking design use some imagination and possibly go wild!
• Must be eye catching!

```html
<!DOCTYPE html>
<html lang="en">
<head>
<meta charset="utf-8">
<title>Brightvale Services – Cleaning Brochure</title>
<link rel="stylesheet" href="https://fonts.googleapis.com/css2?family=Roboto:wght@300;400;500;700;900&display=swap">
<style>
  :root{
    --blue:#2bb4e4;
    --blue-dark:#1f8fc0;
    --yellow:#f2d21a;
    --grey:#aaaaaa;
    --ink:#2b2b2b;
    --text:#6a6a6a;
    --paper:#ffffff;
    --paper-foot:#f4f4f4;
    --backdrop:#e9eaec;
  }
  *{box-sizing:border-box;margin:0;padding:0}
  html,body{width:1200px;height:1000px;overflow:hidden}
  body{background:var(--backdrop);font-family:"Roboto",Arial,sans-serif;color:var(--ink);position:relative}

  .page{position:absolute;background:var(--paper);box-shadow:0 4px 18px rgba(0,0,0,.12);overflow:hidden}

  /* ---------- Cover ---------- */
  .cover{left:60px;top:36px;width:330px;height:467px;background:linear-gradient(#fff 70%,var(--paper-foot))}
  .cover-photo{position:absolute;left:0;top:0;width:100%;height:290px;
    background:linear-gradient(160deg,#9aa3ab 0%,#5c6670 35%,#2f3b52 60%,#49505a 100%)}
  .cover-photo::after{content:"";position:absolute;inset:0;background:rgba(0,0,0,.28)}
  .cover-title{position:absolute;left:0;right:0;top:150px;text-align:center;color:#fff;
    font-weight:500;font-size:17px;line-height:1.15;letter-spacing:.3px;text-transform:uppercase}
  .cover-url{position:absolute;left:0;right:0;top:196px;text-align:center;color:#fff;font-size:7px;font-weight:500}
  .service-tiles{position:absolute;left:14px;right:14px;top:258px;display:flex;align-items:flex-start}
  .tile{flex:1;height:72px;display:flex;flex-direction:column;align-items:center;justify-content:center;gap:5px;
    color:#fff;font-size:7px;line-height:1.2;text-align:center;text-transform:uppercase;margin-top:10px}
  .tile--blue{background:var(--blue)}
  .tile--yellow{background:var(--yellow);color:var(--ink);margin-top:-6px;height:88px}
  .tile svg{width:22px;height:22px}
  .cover-brand{position:absolute;left:0;right:0;top:392px;display:flex;justify-content:center;align-items:center;gap:6px;
    color:var(--blue);font-weight:700;font-size:15px}
  .cover-brand .dot{width:9px;height:9px;border-radius:50%;background:var(--blue)}

  /* ---------- Spread ---------- */
  .spread{position:absolute;left:420px;top:455px;width:730px;height:516px;display:flex;box-shadow:0 4px 18px rgba(0,0,0,.12)}
  .spread .page{position:relative;box-shadow:none;width:365px;height:516px;padding:30px 28px}
  .spread .page--left{background:linear-gradient(90deg,#fff 88%,#ececec)}
  .spread .page--right{background:linear-gradient(270deg,#fff 88%,#ececec)}
  .page-url{font-size:5.5px;font-weight:700;color:var(--ink);position:absolute;top:14px}
  .page--left .page-url{left:28px}
  .page--right .page-url{right:28px}

  .section-head{position:relative;padding-bottom:6px;margin-bottom:8px}
  .section-head::before{content:"";position:absolute;left:0;right:0;top:-8px;height:1px;
    background:linear-gradient(90deg,transparent,var(--yellow) 40%,var(--yellow))}
  .section-head::after{content:"";position:absolute;left:0;bottom:0;width:28px;height:2px;background:var(--blue)}
  .section-title{font-size:13px;font-weight:700;letter-spacing:.2px;text-transform:uppercase}
  .section-sub{font-size:7.5px;color:var(--grey);font-weight:300}

  .body-copy{font-size:5.8px;line-height:1.55;color:var(--text);margin-bottom:6px}
  .call-out{font-size:6px;font-weight:700;margin:10px 0 6px}
  .bullet-grid{display:grid;grid-template-columns:1fr 1fr;gap:5px 10px;margin-bottom:10px}
  .bullet{display:flex;align-items:center;gap:5px;font-size:5.5px;font-weight:700;text-transform:uppercase}
  .bullet::before{content:"";width:9px;height:6px;background:var(--blue);clip-path:polygon(0 0,100% 0,80% 100%,0 100%)}
  .bullet--yellow::before{background:var(--yellow)}

  .photo{border-radius:1px}
  .photo--commercial{width:100%;height:165px;margin-top:6px;
    background:linear-gradient(120deg,#d9dfe4 0%,#9fa9b2 40%,#3c4250 70%,#c8ced4 100%)}

  .intro{font-size:5.8px;color:var(--text);margin:4px 0 10px}
  .reason{display:flex;gap:10px;margin-bottom:10px;align-items:flex-start}
  .reason-badge{flex:none;width:20px;height:20px;background:var(--blue);display:flex;align-items:center;justify-content:center;
    clip-path:polygon(0 0,100% 0,100% 80%,80% 100%,0 100%)}
  .reason-badge svg{width:12px;height:12px}
  .reason-title{font-size:6px;font-weight:700;text-transform:uppercase;margin-bottom:2px}
  .reason-text{font-size:5.5px;color:var(--text);line-height:1.5}
  .reason:nth-child(3){margin-left:10px}
  .reason:nth-child(4){margin-left:20px}

  .oven-section{margin-top:36px;margin-left:34px}
  .oven-photos{display:flex;gap:6px;margin-top:8px}
  .photo--oven{width:100px;height:62px;background:linear-gradient(135deg,#2c2f34 0%,#55585e 50%,#e3c22a 100%)}
  .photo--oven.alt{background:linear-gradient(135deg,#3a3d42 0%,#23262a 55%,#d9b820 100%)}
</style>
</head>
<body>

<section class="page cover">
  <div class="cover-photo" role="img" aria-label="Photo of cleaning staff in blue uniforms wiping desks in a bright office"></div>
  <h1 class="cover-title">Domestic and Commercial<br>Cleaning Services</h1>
  <p class="cover-url">www.brightvaleservices.co.uk</p>

  <div class="service-tiles">
    <div class="tile tile--blue">
      <svg viewBox="0 0 24 24" fill="none" stroke="#fff" stroke-width="1.4"><path d="M8 3v11"/><path d="M8 3h4"/><rect x="5" y="14" width="12" height="6" rx="3"/><circle cx="8" cy="20.5" r="1.2"/><circle cx="15" cy="20.5" r="1.2"/></svg>
      <span>Commercial<br>Cleaning</span>
    </div>
    <div class="tile tile--yellow">
      <svg viewBox="0 0 24 24" fill="none" stroke="#2b2b2b" stroke-width="1.4"><rect x="3" y="5" width="18" height="14"/><rect x="6" y="8" width="12" height="8"/><path d="M3 3v2M7 3v2M11 3v2M15 3v2M19 3v2M3 19v2M7 19v2M11 19v2M15 19v2M19 19v2"/></svg>
      <span>Carpet<br>Cleaning</span>
    </div>
    <div class="tile tile--blue">
      <svg viewBox="0 0 24 24" fill="none" stroke="#fff" stroke-width="1.4"><rect x="3" y="3" width="18" height="18" rx="1"/><path d="M3 8h18"/><rect x="6" y="11" width="12" height="7"/><circle cx="7" cy="5.5" r=".8"/><circle cx="10" cy="5.5" r=".8"/><circle cx="13" cy="5.5" r=".8"/></svg>
      <span>Oven<br>Cleaning</span>
    </div>
  </div>

  <div class="cover-brand"><span class="dot"></span><span>Brightvale</span></div>
</section>

<div class="spread">
  <section class="page page--left">
    <p class="page-url">www.brightvaleservices.co.uk</p>
    <header class="section-head" style="margin-top:34px">
      <h2 class="section-title">Commercial Cleaning in York</h2>
      <p class="section-sub">Paying too much for too little? Why not try Brightvale?</p>
    </header>
    <p class="body-copy">We create bespoke packages to suit each individual businesses needs. Whether you require cleaning daily, weekly, fortnightly or monthly we are happy to create a bespoke package for you.</p>
    <p class="body-copy">Brightvale Services constantly strives to be the most efficient and effective commercial cleaning service in York. We are accustomed to managing a diverse array of accounts, from large organisations to family businesses.</p>
    <p class="body-copy">We understand that the size of the business alone doesn't define the nature and complexity of the cleaning tasks required. Therefore, we hold thorough discussions with operations management and carry out a cleaning requirements audit of the premises before initiating the contract.</p>
    <p class="call-out">Contact us today for a free no obligation quotation!</p>
    <div class="bullet-grid">
      <span class="bullet bullet--yellow">Hassle free contract transfer (TUPE)</span>
      <span class="bullet">Bespoke packages</span>
      <span class="bullet bullet--yellow">Value for money</span>
    </div>
    <div class="photo photo--commercial" role="img" aria-label="Photo of cleaners vacuuming and wiping glass partitions in an office"></div>
  </section>

  <section class="page page--right">
    <p class="page-url">www.brightvaleservices.co.uk</p>
    <header class="section-head" style="margin-top:34px">
      <h2 class="section-title">Carpet Cleaning</h2>
      <p class="section-sub">If you are looking for carpet cleaning, we've got you covered</p>
    </header>
    <div class="reasons">
      <p class="intro">Here are some of the main reasons to choose Brightvale Services.</p>
      <div class="reason">
        <span class="reason-badge"><svg viewBox="0 0 24 24" fill="none" stroke="#fff" stroke-width="2"><circle cx="12" cy="12" r="9"/><path d="M8 12l3 3 5-6"/></svg></span>
        <div><p class="reason-title">Free no-obligation quote</p><p class="reason-text">We'll give you the information you need to make<br>an informed decision with no hard sell.</p></div>
      </div>
      <div class="reason">
        <span class="reason-badge"><svg viewBox="0 0 24 24" fill="none" stroke="#fff" stroke-width="2"><circle cx="12" cy="12" r="9"/><path d="M8 12l3 3 5-6"/></svg></span>
        <div><p class="reason-title">Specialist staff with specialist equipment</p><p class="reason-text">Our staff are fully trained with the best tools<br>available for the job.</p></div>
      </div>
      <div class="reason">
        <span class="reason-badge"><svg viewBox="0 0 24 24" fill="none" stroke="#fff" stroke-width="2"><circle cx="12" cy="12" r="9"/><path d="M8 12l3 3 5-6"/></svg></span>
        <div><p class="reason-title">Flexible and convenient</p><p class="reason-text">Fast drying time and flexible bookings mean that<br>we can fit your schedule.</p></div>
      </div>
    </div>

    <div class="oven-section">
      <header class="section-head">
        <h2 class="section-title">Oven Cleaning</h2>
        <p class="section-sub">In partnership with Oven Renew</p>
      </header>
      <p class="body-copy">Tenants, landlords and agents alike.</p>
      <p class="body-copy">Yorkshire's leading oven cleaning and repair specialists. Have your oven cleaned from as little as £45.00 (inc vat).</p>
      <div class="oven-photos">
        <div class="photo photo--oven" role="img" aria-label="Photo of a gloved hand cleaning an oven interior"></div>
        <div class="photo photo--oven alt" role="img" aria-label="Photo of a yellow glove scrubbing an oven hob"></div>
      </div>
    </div>
  </section>
</div>

</body>
</html>
```